731 Orchard Avenue Residences

designing a sign for apartment complex;
prefer colors gray white and yellow

Target Market(s)

residents coming home to their apartment

Font styles to use
Serif
Sans Serif

Colors
FFF300
FFF600
FEFA6F
FFFEC7
FFFEE8

Requirements
Must have
• black or gray, white and some yellow; easy to read and see

```html
<!DOCTYPE html>
<html lang="en">
<head>
<meta charset="utf-8">
<title>731 Orchard Avenue Residences – Entrance Sign</title>
<link href="https://fonts.googleapis.com/css2?family=Cinzel:wght@400;700&family=Pinyon+Script&display=swap" rel="stylesheet">
<style>
  :root {
    --sign-yellow: #fff300;
    --sign-gray: #4d4d4d;
    --sign-white: #ffffff;
    --backdrop: #f2f2ee;
  }
  html, body {
    margin: 0;
    padding: 0;
    width: 1200px;
    height: 800px;
    overflow: hidden;
    background: var(--backdrop);
  }
  .canvas {
    position: relative;
    width: 1200px;
    height: 800px;
    display: flex;
    align-items: center;
    justify-content: center;
  }
  .sign {
    width: 1048px;
    height: 722px;
    display: block;
  }
  .sign-border { fill: var(--sign-yellow); }
  .sign-face { fill: var(--sign-gray); }
  .sign-inline { fill: none; stroke: var(--sign-white); stroke-width: 3; }
  .sign-rule { stroke: var(--sign-yellow); stroke-width: 2; }
  .street-number {
    font-family: "Cinzel", serif;
    font-weight: 700;
    font-size: 250px;
    fill: var(--sign-white);
  }
  .street-name {
    font-family: "Cinzel", serif;
    font-weight: 400;
    font-size: 104px;
    letter-spacing: 4px;
    fill: var(--sign-white);
  }
  .property-type {
    font-family: "Pinyon Script", cursive;
    font-size: 84px;
    fill: var(--sign-white);
  }
  .greeting {
    font-family: "Cinzel", serif;
    font-weight: 400;
    font-size: 74px;
    letter-spacing: 2px;
    fill: var(--sign-white);
  }
</style>
</head>
<body>
<main class="canvas">
  <svg class="sign" viewBox="508 240 1310 902" role="img" aria-label="731 Orchard Avenue Residences – Welcome">
    <path class="sign-border" d="M508 500 H605 C700 340 920 240 1165 240 C1410 240 1640 340 1733 500 H1818 V1142 H508 Z"/>
    <path class="sign-face" d="M589 581 H654 C740 420 940 322 1165 322 C1390 322 1600 420 1684 581 H1738 V1062 H589 Z"/>
    <path class="sign-inline" d="M625 620 H678 C740 460 950 358 1165 358 C1380 358 1600 460 1660 620 H1701 V1026 H625 Z"/>

    <text class="street-number" x="1165" y="645" text-anchor="middle">731</text>
    <text class="street-name" x="1165" y="788" text-anchor="middle">Orchard Avenue</text>
    <text class="property-type" x="1165" y="870" text-anchor="middle">Residences</text>

    <line class="sign-rule" x1="672" y1="965" x2="958" y2="965"/>
    <text class="greeting" x="1160" y="990" text-anchor="middle">Welcome</text>
    <line class="sign-rule" x1="1358" y1="965" x2="1645" y2="965"/>
  </svg>
</main>
</body>
</html>
```